1 Page Website Responsive HTML Refresh

My website was designed on the fly and is not representative of our brand in the market. (www.tarravalehub.com.au)

I have a coder who can turn your design into real life - I just need the PSD files created for him to work to. It should align to our corporate flyer - I have attached the files.

The site should just be a single page and has 4 sections:

1. Hero Image and Intro
2. For Businesses
3. For Residents
4. Contact

The content can be taken from the live website, however there are a few changes to be made, that will impact your design:

For Businesses: Remove the call to action email box and all the content that is about "Just for Small Business"

For Residents: Remove #3 Product Diversity, so there are just 4 reasons.

Please add in a section that shows the areas that Tarravale Hub is currently active in. These are:

Indooroopilly & Surrounds
Ascot & Surrounds
North Lakes & Surrounds
South Brisbane & Surrounds
Springfield & Surrounds
Browns Plains & Surrounds
Redcliffe & Surrounds

I am looking for something clean and modern that is aligned to our flyer.

Target Market(s)

Small business owners reviewing the site to establish credibility with our business.

Industry/Entity Type

Advertising

Number of Pages Required

1 page

Font styles to use
Sans Serif

Colors
abd036

Requirements
Must have
• The site must include an image of the publication so people see what it looks like and a sample of the FB page image too (images are in attachment)
• Must use my corporate colour of green as the major highlight colour.
Nice to have
• Open to clean, modern and professional design. Good use of white space. Not cluttered or too busy

```html
<!DOCTYPE html>
<html lang="en">
<head>
<meta charset="utf-8">
<title>Tarravale Hub – Connecting Local Businesses with Local Residents</title>
<link rel="stylesheet" href="https://fonts.googleapis.com/css2?family=Oswald:wght@300;400;500;600&family=Open+Sans:ital,wght@0,400;0,600;0,700;1,700&display=swap">
<style>
:root{
  --green:#abd036;
  --green-dark:#8fb322;
  --ink:#333333;
  --text:#666666;
  --muted:#8a8a8a;
  --black:#111111;
  --bar:#2b2b2b;
  --paper:#ffffff;
  --soft:#f2f2f2;
  --rule:#cfcfcf;
}
*{box-sizing:border-box;margin:0;padding:0}
html,body{width:1200px;height:3758px;overflow:hidden;background:var(--paper)}
body{font-family:"Open Sans",Arial,sans-serif;color:var(--text);position:relative}

/* top bar */
.topbar{position:absolute;top:0;left:0;width:1200px;height:45px;background:var(--bar);color:#ddd;font-size:14px}
.topbar .item{position:absolute;top:12px;display:flex;align-items:center;gap:10px}
.topbar .badge{width:22px;height:22px;border-radius:3px;background:var(--green);display:flex;align-items:center;justify-content:center}
.topbar .phone{left:706px}
.topbar .email{left:876px}

/* nav */
.nav{position:absolute;top:45px;left:0;width:1200px;height:110px;background:var(--paper)}
.brand{position:absolute;left:88px;top:30px;display:flex;align-items:center;gap:12px}
.brand .dot{width:48px;height:48px;border-radius:50%;background:var(--green)}
.brand .name{font-family:"Oswald",sans-serif;font-weight:500;font-size:32px;color:var(--green);letter-spacing:.5px}
.menu{position:absolute;top:46px;left:664px;display:flex;gap:44px;font-size:13px;font-weight:700;color:var(--ink);text-transform:uppercase;list-style:none}

/* hero */
.hero{position:absolute;top:155px;left:0;width:1200px;height:597px;
  background:linear-gradient(180deg,#4c7db8 0%,#8fb3d8 30%,#b7c4cf 52%,#6f7a82 70%,#3f4a52 84%,#2a2f33 100%)}
.hero h1{position:absolute;top:86px;left:0;width:1200px;text-align:center;white-space:nowrap;font-family:"Oswald",sans-serif;font-weight:500;font-size:68px;color:#fff;letter-spacing:1px;text-transform:uppercase;line-height:1}
.hero .sub{position:absolute;top:196px;left:0;width:1200px;text-align:center;white-space:nowrap;font-family:"Oswald",sans-serif;font-size:26px;color:#fff;letter-spacing:1px;text-transform:uppercase}
.hero .buttons{position:absolute;top:392px;left:436px;display:flex}
.btn{display:block;height:38px;line-height:38px;font-size:12px;font-weight:700;color:#fff;text-transform:uppercase;text-decoration:none;text-align:center}
.btn.dark{background:var(--black);width:165px}
.btn.light{background:var(--green);width:163px}
.hero .mark{position:absolute;left:560px;top:510px;width:80px;height:80px;border-radius:50%;background:var(--green)}

/* intro band */
.intro{position:absolute;top:752px;left:0;width:1200px;height:175px;background:var(--black);color:#fff;text-align:center}
.intro p{position:absolute;top:28px;left:110px;width:980px;font-size:13.5px;line-height:20px}
.intro .tagline{position:absolute;top:122px;left:0;width:1200px;font-style:italic;font-weight:700;font-size:22px;color:var(--green);text-transform:uppercase;letter-spacing:.5px}
.notch{position:absolute;left:570px;width:0;height:0;border-left:30px solid transparent;border-right:30px solid transparent}
.intro .notch{top:175px;border-top:32px solid var(--black)}

/* section headings */
.heading{position:absolute;left:0;width:1200px;text-align:center;font-family:"Oswald",sans-serif;font-weight:300;font-size:38px;line-height:48px;color:var(--ink);text-transform:uppercase;letter-spacing:.5px}
.heading em{font-style:normal;color:var(--green)}
.heading::after{content:"";display:block;width:58px;height:3px;background:var(--green);margin:10px auto 0}

/* businesses */
.biz-lead{position:absolute;top:1082px;left:130px;width:940px;text-align:center;font-size:13.5px;line-height:21px}
.dashed{position:absolute;left:88px;width:1022px;border-top:1px dashed var(--rule)}
.questions{position:absolute;top:1262px;left:100px;list-style:none;font-family:"Oswald",sans-serif;font-size:19px;text-transform:uppercase;letter-spacing:.3px;line-height:29.5px}
.questions li{display:flex;align-items:center;gap:14px;color:var(--green)}
.questions li.dark{color:var(--ink)}
.questions li::before{content:"";width:8px;height:8px;border-radius:50%;background:var(--green)}
.photo{position:absolute;border-radius:50%;border:4px solid #fff;box-shadow:0 0 0 1px #ddd}

/* reasons grids */
.reasons{position:absolute;display:grid}
.reason{display:flex;gap:18px}
.reason svg{flex:none;margin-top:6px}
.reason h3{font-family:"Oswald",sans-serif;font-weight:500;font-size:15px;color:var(--green);text-transform:uppercase;letter-spacing:.4px;margin-bottom:8px}
.reason p{font-size:11.5px;line-height:17px;color:var(--muted)}
.six{top:1622px;left:92px;grid-template-columns:repeat(3,340px);grid-auto-rows:163px}
.six .reason p{width:240px}
.four{top:2530px;left:92px;grid-template-columns:repeat(2,510px);grid-auto-rows:140px}
.four .reason p{width:420px}

/* residents */
.residents{position:absolute;top:1949px;left:0;width:1200px;height:401px;background:var(--soft)}
.residents .copy{position:absolute;top:125px;left:93px;width:780px;font-size:13.5px;line-height:22px}
.residents .impact{position:absolute;top:300px;left:93px;width:620px;font-weight:700;font-size:17px;line-height:26px;color:var(--green);text-transform:uppercase}
.residents .notch{top:401px;border-top:30px solid var(--soft)}
.publication{position:absolute;left:880px;top:50px;width:190px;height:190px;border-radius:50%;background:linear-gradient(135deg,#fafafa,#e6e6e6 55%,#c9d88f);border:6px solid #fff;box-shadow:0 0 0 1px #ccc}

/* areas */
.areas{position:absolute;top:2880px;left:0;width:396px;height:326px;background:#f7f7f7}
.areas h2{position:absolute;top:20px;left:90px;width:290px;font-family:"Oswald",sans-serif;font-weight:400;font-size:19px;color:var(--ink);text-transform:uppercase;border-bottom:1px solid var(--ink);padding-bottom:4px;white-space:nowrap}
.areas ul{position:absolute;top:66px;left:92px;list-style:none;font-size:13px;color:var(--ink);line-height:32px}
.areas li{display:flex;align-items:center;gap:12px}
.areas li::before{content:"";width:7px;height:7px;border-radius:50%;background:var(--green)}
.map{position:absolute;top:2880px;left:396px;width:804px;height:326px;background:linear-gradient(160deg,#efe9dc 0%,#e4e2d8 45%,#d9e3d2 70%,#c9d9e6 100%)}

/* contact */
.contact{position:absolute;top:3206px;left:0;width:1200px;height:439px;background:linear-gradient(180deg,#3c3a31 0%,#5a5444 40%,#4a5a3c 75%,#36402c 100%)}
.form{position:absolute;top:50px;left:118px;width:522px}
.field{display:block;border:1px solid rgba(255,255,255,.35);background:rgba(0,0,0,.35);color:#eee;font-size:11px;padding:10px 12px}
.row{display:flex;gap:8px;margin-bottom:8px}
.row .field{flex:1;height:38px}
.field.full{height:38px;margin-bottom:8px}
.field.message{height:170px;margin-bottom:12px}
.send{display:block;width:522px;height:36px;line-height:36px;background:var(--green);color:var(--black);text-align:center;font-size:12px;font-weight:700;text-transform:uppercase}
.details{position:absolute;top:56px;left:646px;color:#fff;font-size:12px;line-height:19px}
.details h2{font-family:"Oswald",sans-serif;font-weight:400;font-size:30px;color:var(--green);text-transform:uppercase;margin-bottom:22px}
.details h4{font-size:12px;font-weight:700;color:var(--green);text-transform:uppercase;margin-top:12px}

/* footer */
.footer{position:absolute;top:3645px;left:0;width:1200px;height:113px;background:var(--paper)}
.social{position:absolute;top:32px;left:464px;display:flex;gap:28px;list-style:none}
.social li{width:22px;height:22px;border-radius:50%;background:var(--black)}
.copyright{position:absolute;top:76px;left:0;width:1200px;text-align:center;font-size:11px;color:var(--ink)}
</style>
</head>
<body>

<header>
  <div class="topbar">
    <div class="item phone"><span class="badge"><svg width="12" height="12" viewBox="0 0 24 24"><path d="M6.6 10.8a15 15 0 0 0 6.6 6.6l2.2-2.2a1 1 0 0 1 1-.25 11.4 11.4 0 0 0 3.6.57 1 1 0 0 1 1 1V20a1 1 0 0 1-1 1A17 17 0 0 1 3 4a1 1 0 0 1 1-1h3.5a1 1 0 0 1 1 1c0 1.25.2 2.45.57 3.57a1 1 0 0 1-.25 1z" fill="#2b2b2b"/></svg></span>1300 555 014</div>
    <div class="item email"><span class="badge"><svg width="12" height="10" viewBox="0 0 24 18"><rect x="1" y="1" width="22" height="16" fill="none" stroke="#2b2b2b" stroke-width="2.5"/><path d="M1 1l11 9 11-9" fill="none" stroke="#2b2b2b" stroke-width="2.5"/></svg></span>info@tarravalehub.com.au</div>
  </div>
  <nav class="nav">
    <div class="brand"><span class="dot"></span><span class="name">Tarravale Hub</span></div>
    <ul class="menu"><li>Home</li><li>For Businesses</li><li>For Residents</li><li>Contact</li></ul>
  </nav>
</header>

<section class="hero" role="img" aria-label="Photograph of a city skyline with a steel bridge over the river">
  <h1>It’s time to choose Tarravale Hub</h1>
  <p class="sub">Connecting local businesses with local residents</p>
  <div class="buttons"><a class="btn dark">For Businesses</a><a class="btn light">For Residents</a></div>
  <span class="mark"></span>
</section>

<section class="intro">
  <p>A vibrant community is such a huge part of the social fabric of our world.<br>By engaging with the people who work and live around you, you can actively contribute to making your local area a better place. Tarravale Hub is a platform that helps connect local businesses with local residents. It offers a cost-effective way for business owners to communicate with their ideal customers, and provides information, news and special offers that are relevant to the people who live in the area.</p>
  <div class="tagline">Choose Tarravale Hub &amp; connect with your community</div>
  <span class="notch"></span>
</section>

<section class="businesses">
  <h2 class="heading" style="top:990px"><em>For</em> Businesses</h2>
  <p class="biz-lead">Tarravale Hub is a marketing and advertising solution designed just for small business. Combining expert guidance around marketing strategy, with locally focused digital and print advertising, Tarravale Hub provides a holistic and cost-effective solution that is revolutionising the way small businesses connect with their potential customers.</p>
  <div class="dashed" style="top:1202px"></div>
  <ul class="questions">
    <li>Want a way to connect with customers in your local area?</li>
    <li class="dark">Wish there was a more cost-effective way to advertise your business?</li>
    <li>Struggle to find the time to tackle marketing?</li>
    <li class="dark">Need some advice from a marketing professional?</li>
    <li>Know you need to be doing more marketing?</li>
  </ul>
  <div class="photo" role="img" aria-label="Round portrait photo of a team member" style="left:822px;top:1238px;width:116px;height:116px;background:linear-gradient(160deg,#6a8fb0,#c7b39c)"></div>
  <div class="photo" role="img" aria-label="Round portrait photo of a team member" style="left:948px;top:1238px;width:116px;height:116px;background:linear-gradient(160deg,#d8d2c4,#c9a886)"></div>
  <div class="photo" role="img" aria-label="Round portrait photo of a team member" style="left:850px;top:1320px;width:112px;height:112px;background:linear-gradient(160deg,#9aa3ab,#b89a80)"></div>
  <div class="dashed" style="top:1448px"></div>

  <h2 class="heading" style="top:1498px"><em>6 Reasons</em> your business needs Tarravale Hub</h2>
  <div class="reasons six">
    <div class="reason">
      <svg width="40" height="32" viewBox="0 0 40 32"><path d="M4 12h8l18-10v28L12 20H4z" fill="var(--green)"/><rect x="8" y="20" width="6" height="10" fill="var(--green)"/></svg>
      <div><h3>Marketing + Advertising</h3><p>Combines both marketing strategy and advertising execution to provide a more cohesive and effective way to promote your business.</p></div>
    </div>
    <div class="reason">
      <svg width="40" height="32" viewBox="0 0 40 32"><rect x="2" y="6" width="32" height="20" rx="2" fill="var(--green)"/><circle cx="18" cy="16" r="6" fill="#fff"/><text x="18" y="20" font-size="10" text-anchor="middle" fill="var(--green)" font-family="Arial">$</text></svg>
      <div><h3>Small Business Value</h3><p>Fully inclusive of consulting, design and production and it costs less than 10c per household.</p></div>
    </div>
    <div class="reason">
      <svg width="40" height="32" viewBox="0 0 40 32"><path d="M4 4h32l3 8H1z" fill="var(--green)"/><rect x="5" y="14" width="30" height="16" fill="var(--green)"/><rect x="16" y="18" width="8" height="12" fill="#fff"/></svg>
      <div><h3>Showcasing your business</h3><p>Focuses on your story as well as your products and services to help you really connect with your local customer base.</p></div>
    </div>
    <div class="reason">
      <svg width="40" height="32" viewBox="0 0 40 32"><rect x="2" y="5" width="34" height="24" fill="var(--green)"/><path d="M2 5l17 13L36 5" fill="none" stroke="#fff" stroke-width="2.5"/></svg>
      <div><h3>Direct mail + social media</h3><p>Leverages the most cost effective and proven online and offline methods to get your brand out in the market.</p></div>
    </div>
    <div class="reason">
      <svg width="40" height="32" viewBox="0 0 40 32"><circle cx="20" cy="9" r="6" fill="var(--green)"/><path d="M9 28c0-8 5-12 11-12s11 4 11 12z" fill="var(--green)"/><circle cx="7" cy="12" r="4" fill="var(--green)"/><circle cx="33" cy="12" r="4" fill="var(--green)"/><path d="M0 26c0-6 3-9 7-9s5 2 5 2L9 26z" fill="var(--green)"/><path d="M40 26c0-6-3-9-7-9s-5 2-5 2l3 7z" fill="var(--green)"/></svg>
      <div><h3>Your ideal customer</h3><p>Targets only people in your local area so you can create long term relationships and repeat business.</p></div>
    </div>
    <div class="reason">
      <svg width="40" height="32" viewBox="0 0 40 32"><circle cx="18" cy="16" r="14" fill="none" stroke="var(--green)" stroke-width="3"/><circle cx="18" cy="16" r="8" fill="none" stroke="var(--green)" stroke-width="3"/><circle cx="18" cy="16" r="3" fill="var(--green)"/><path d="M18 16L36 2" stroke="var(--green)" stroke-width="2.5"/></svg>
      <div><h3>Rely on the experts</h3><p>Makes your advertising and marketing activities effective, easy and stress free, allowing you to focus on running your business.</p></div>
    </div>
  </div>
</section>

<section class="residents">
  <h2 class="heading" style="top:55px"><em>For</em> Residents</h2>
  <p class="copy">Keep a look out in your letterbox each quarter for Tarravale Hub. It’s jam packed with offers and details on businesses that are just around the corner from you. With Tarravale Hub you can get to know the staff who serve you, find out about new products and services and learn what businesses are doing to support your local area. For detailed information on what is happening in your neighbourhood delivered digitally, be sure to follow the Tarravale Hub community page for your area. This page is like a community hub where you can find details on events, news that is locally focused, extra specials and deals local businesses want to share, and the chance to win prizes.</p>
  <p class="impact">Your support of local businesses has a very real and tangible impact on your neighborhood.</p>
  <div class="publication" role="img" aria-label="Photo of the printed quarterly publication fanned open"></div>
  <span class="notch"></span>
</section>

<section class="why">
  <h2 class="heading" style="top:2405px"><em>4 Reasons</em> why it is great to choose Tarravale Hub</h2>
  <div class="reasons four">
    <div class="reason">
      <svg width="46" height="34" viewBox="0 0 46 34"><circle cx="23" cy="9" r="7" fill="var(--green)"/><path d="M10 32c0-9 6-14 13-14s13 5 13 14z" fill="var(--green)"/><circle cx="7" cy="13" r="5" fill="var(--green)"/><circle cx="39" cy="13" r="5" fill="var(--green)"/><path d="M0 30c0-6 3-10 7-10s6 3 6 3l-3 7z" fill="var(--green)"/><path d="M46 30c0-6-3-10-7-10s-6 3-6 3l3 7z" fill="var(--green)"/></svg>
      <div><h3>Unique communities</h3><p>You chose to live in your area because it offered something unique that resonated with you. It had lots of great parks, was in the catchment of a great school, or maybe it had good coffee a stone’s throw away. That unique feel of a local area is in part shaped by the businesses that trade there.</p></div>
    </div>
    <div class="reason">
      <svg width="46" height="34" viewBox="0 0 46 34"><circle cx="20" cy="17" r="16" fill="var(--green)"/><text x="20" y="24" font-size="20" font-weight="700" text-anchor="middle" fill="#fff" font-family="Arial">$</text></svg>
      <div><h3>Keeping dollars local</h3><p>Locally owned businesses understand how important it is to support other businesses like them. They are more likely to spend a larger share of their revenue in their own backyards, further enriching the whole community and keeping the cycle of local spending going.</p></div>
    </div>
    <div class="reason">
      <svg width="46" height="34" viewBox="0 0 46 34"><rect x="4" y="10" width="34" height="22" rx="3" fill="var(--green)"/><path d="M14 10V5h14v5" fill="none" stroke="var(--green)" stroke-width="3"/></svg>
      <div><h3>Local jobs</h3><p>It makes sense that a locally owned business creates more jobs locally. This means there are more opportunities to work closer to home and your kids have more chances for their first jobs.</p></div>
    </div>
    <div class="reason">
      <svg width="46" height="34" viewBox="0 0 46 34"><path d="M20 32S3 21 3 11a8 8 0 0 1 17-3 8 8 0 0 1 17 3c0 10-17 21-17 21z" fill="var(--green)"/></svg>
      <div><h3>Giving back</h3><p>You only need to see the certificates proudly placed on the walls of local businesses to know they are the ones sponsoring the local soccer club and donating prizes to the school fund raiser. Your support of them helps them support causes in your neighbourhood.</p></div>
    </div>
  </div>
</section>

<section class="areas">
  <h2>Tarravale Hub is currently active in</h2>
  <ul>
    <li>Indooroopilly &amp; Surrounds</li>
    <li>Ascot &amp; Surrounds</li>
    <li>North Lakes &amp; Surrounds</li>
    <li>South Brisbane &amp; Surrounds</li>
    <li>Springfield &amp; Surrounds</li>
    <li>Browns Plains &amp; Surrounds</li>
    <li>Redcliffe &amp; Surrounds</li>
  </ul>
</section>
<div class="map" role="img" aria-label="Street map of the greater city area with markers on each active suburb"></div>

<section class="contact" role="img" aria-label="Aerial photo of suburban rooftops and trees">
  <form class="form">
    <div class="row"><span class="field">Name</span><span class="field">Email</span></div>
    <span class="field full">Subject</span>
    <span class="field message">Message</span>
    <span class="send">Send Now</span>
  </form>
  <div class="details">
    <h2>Contact Us</h2>
    <h4>Office Address:</h4>
    <p>PO Box 142, Carrow QLD 4010<br>ABN: 00 000 000 000</p>
    <h4>Phone:</h4>
    <p>1300 555 014</p>
    <h4>Email:</h4>
    <p>info@tarravalehub.com.au</p>
  </div>
</section>

<footer class="footer">
  <ul class="social" aria-label="Social media links"><li></li><li></li><li></li><li></li><li></li><li></li></ul>
  <p class="copyright">© all Rights Reserved , Tarravale Hub</p>
</footer>

</body>
</html>
```